Online Sports Booking Business

We need a flyer design for a new company based in Bahrain called "GoalDash.net".

GoalDash is an online booking service for the sport field in Bahrain. We would like to design a flyer in away that reflects our idea and the type of customers who will benefit from the service. You can visit the website in order to get an idea about the service provided.

Service Description:
Simply sign up, search and choose, book and pay for any sports venue or activity using your own computer or smartphone.

- Choose from different sport centers and activities in Bahrain
- Compare based on unbiased reviews by real people
- Check for availability
- Book and pay online in less than a minute
- Track, manage, modify and cancel your bookings online
- Receive automatic notifications (upon request) whenever your favorite venue/activity is available
- Rate and post reviews about your experience

We would like the design to use the color green as a background, nice and casual visual icons and images to show the above steps. The final design should communicate the value and benefits in a joyful and casual way that is attractive to the sport lovers.
Updates

Target Market(s)

english speakers aged 18-45 who are into sports.

Industry/Entity Type

Computer

Font styles to use
Sans Serif
Other font styles liked:
• something similar to the logo

Colors
add136
9bcb3c
ffffff

Requirements
Must have
• Please use the content in the attachment. Logo can be taken from goaldash.net
Nice to have
• steps and benefits to use icons and visual presentations rather than dull text only.

```html
<!DOCTYPE html>
<html lang="en">
<head>
<meta charset="utf-8">
<title>GoalDash.net — Services</title>
<link rel="stylesheet" href="https://fonts.googleapis.com/css2?family=Alfa+Slab+One&family=Comfortaa:wght@400;700&display=swap">
<style>
  :root {
    --bar-dark: #1f1f1f;
    --bar-mid: #2c2c2c;
    --lime: #add136;
    --leaf: #9bcb3c;
    --grass-light: #6fbf2a;
    --grass-dark: #2f7a12;
    --title-green: #3f6a14;
    --chalk: #f2f4ef;
    --chalk-shade: #d9ddd3;
    --ink: #1e2a0c;
    --white: #ffffff;
  }
  * { box-sizing: border-box; margin: 0; padding: 0; }
  html, body { width: 849px; height: 1200px; overflow: hidden; background: #ffffff; }
  .flyer {
    position: relative; width: 849px; height: 1200px; overflow: hidden;
    background: radial-gradient(ellipse at 60% 40%, var(--grass-light), var(--grass-dark));
    font-family: "Comfortaa", sans-serif;
  }
  .top-bar {
    position: absolute; left: 0; top: 0; width: 849px; height: 147px;
    background: linear-gradient(180deg, var(--bar-mid), var(--bar-dark));
  }
  .brand { position: absolute; left: 42px; top: 34px; display: flex; align-items: center; gap: 14px; }
  .brand-dot { width: 42px; height: 42px; border: 3px solid var(--white); border-radius: 50%; }
  .brand-name { font-weight: 700; font-size: 40px; color: var(--white); letter-spacing: -0.5px; }
  .brand-tagline { position: absolute; left: 104px; top: 86px; font-weight: 700; font-size: 14px; color: var(--lime); }

  .chalk-lane {
    position: absolute; left: 0; top: 147px; width: 849px; height: 948px;
    background: linear-gradient(90deg, var(--chalk-shade), var(--chalk) 30%, var(--chalk) 75%, var(--chalk-shade));
    clip-path: polygon(30px 0, 452px 0, 496px 948px, 14px 948px);
  }
  .balls-art {
    position: absolute; left: 615px; top: 248px; width: 234px; height: 847px;
    background: linear-gradient(180deg, #e9e9e9 0%, #c9c9c9 22%, #b5562a 30%, #8a3d1c 48%, #ecebe6 58%, #d9e63a 72%, #c8d62c 84%, #f2f2f2 94%);
    border-radius: 117px 0 0 117px;
    opacity: 0.95;
  }
  .section-title {
    position: absolute; left: 120px; top: 180px;
    font-family: "Alfa Slab One", serif; font-weight: 400; font-size: 60px; line-height: 1;
    color: var(--title-green);
  }
  .service {
    position: absolute; display: flex; align-items: center;
    background: linear-gradient(180deg, var(--lime), var(--leaf));
    box-shadow: 4px 5px 6px rgba(0,0,0,0.45);
  }
  .service-icon { width: 82px; flex: 0 0 82px; display: flex; justify-content: center; }
  .service-text { font-size: 17px; line-height: 1.3; color: var(--ink); padding-right: 14px; }
  .s1 { left: 110px; top: 273px; width: 318px; height: 84px; }
  .s2 { left: 110px; top: 374px; width: 318px; height: 85px; }
  .s3 { left: 110px; top: 477px; width: 322px; height: 89px; }
  .s4 { left: 95px;  top: 585px; width: 340px; height: 98px; }
  .s5 { left: 93px;  top: 699px; width: 342px; height: 99px; }
  .s6 { left: 86px;  top: 816px; width: 356px; height: 110px; }
  .s6 .service-text { font-size: 15px; line-height: 1.25; padding-right: 10px; }
  .s7 { left: 78px;  top: 945px; width: 363px; height: 113px; }
  .s4 .service-icon, .s5 .service-icon, .s7 .service-icon { width: 100px; flex-basis: 100px; }
  .s6 .service-icon { width: 90px; flex-basis: 90px; }

  .bottom-bar {
    position: absolute; left: 0; top: 1095px; width: 849px; height: 105px;
    background: linear-gradient(180deg, var(--bar-mid), var(--bar-dark));
    display: flex; align-items: center; gap: 48px; padding-left: 122px;
    color: var(--white); font-size: 26px;
  }
  .contact { display: flex; align-items: center; gap: 14px; }
</style>
</head>
<body>
<main class="flyer">
  <header class="top-bar">
    <div class="brand"><span class="brand-dot"></span><span class="brand-name">GoalDash.net</span></div>
    <div class="brand-tagline">Online Pitch Booking</div>
  </header>

  <div class="chalk-lane"></div>
  <div class="balls-art" role="img" aria-label="Stack of sports balls: football, basketball, baseball, tennis ball and golf ball"></div>

  <h1 class="section-title">Services</h1>

  <section class="service s1">
    <div class="service-icon">
      <svg width="60" height="44" viewBox="0 0 60 44"><rect x="4" y="2" width="52" height="32" rx="2" fill="#222"/><rect x="8" y="6" width="44" height="24" fill="#e8e8e8"/><rect x="26" y="34" width="8" height="5" fill="#333"/><rect x="16" y="39" width="28" height="3" fill="#222"/></svg>
    </div>
    <p class="service-text">Choose from different sport centers and activities in Bahrain.</p>
  </section>

  <section class="service s2">
    <div class="service-icon">
      <svg width="60" height="46" viewBox="0 0 60 46"><path d="M4 4h32v20H16l-8 7v-7H4z" fill="#333"/><path d="M22 16h34v20h-4v7l-8-7H22z" fill="#f4f4f4" stroke="#555" stroke-width="1.5"/></svg>
    </div>
    <p class="service-text">Compare based on unbiased reviews by real people.</p>
  </section>

  <section class="service s3">
    <div class="service-icon">
      <svg width="56" height="50" viewBox="0 0 56 50"><rect x="3" y="6" width="50" height="42" rx="3" fill="#f4f4f4" stroke="#333" stroke-width="2"/><rect x="3" y="6" width="50" height="10" fill="#333"/><g fill="#888"><rect x="9" y="21" width="6" height="5"/><rect x="19" y="21" width="6" height="5"/><rect x="29" y="21" width="6" height="5"/><rect x="39" y="21" width="6" height="5"/><rect x="9" y="31" width="6" height="5"/><rect x="29" y="31" width="6" height="5"/><rect x="39" y="31" width="6" height="5"/><rect x="9" y="40" width="6" height="5"/><rect x="19" y="40" width="6" height="5"/></g><circle cx="22" cy="33" r="4" fill="#4a9a1c"/></svg>
    </div>
    <p class="service-text">Check for availability</p>
  </section>

  <section class="service s4">
    <div class="service-icon">
      <svg width="78" height="56" viewBox="0 0 78 56"><circle cx="56" cy="16" r="13" fill="#ddd" stroke="#333" stroke-width="2"/><path d="M56 8v8h6" stroke="#333" stroke-width="2" fill="none"/><rect x="2" y="22" width="62" height="20" fill="#111"/><text x="8" y="36" font-family="Comfortaa, sans-serif" font-size="11" fill="#fff">Book now</text><path d="M44 36l0 16 4-4 3 6 3-1-3-6 5 0z" fill="#fff" stroke="#111" stroke-width="1.2"/></svg>
    </div>
    <p class="service-text">Book and pay online in less than a minute</p>
  </section>

  <section class="service s5">
    <div class="service-icon">
      <svg width="70" height="62" viewBox="0 0 70 62"><g fill="none" stroke="#fff" stroke-width="4"><path d="M12 24a24 24 0 0 1 40-12"/><path d="M58 38a24 24 0 0 1-40 12"/></g><path d="M50 4l6 12-13 0z" fill="#fff"/><path d="M20 58l-6-12 13 0z" fill="#fff"/><path d="M24 20l22 22M46 20L24 42" stroke="#222" stroke-width="4"/></svg>
    </div>
    <p class="service-text">Track, manage, modify and cancel your bookings online</p>
  </section>

  <section class="service s6">
    <div class="service-icon">
      <svg width="40" height="66" viewBox="0 0 40 66"><rect x="2" y="2" width="36" height="62" rx="6" fill="#111"/><rect x="6" y="10" width="28" height="44" fill="#2b2b2b"/><circle cx="20" cy="32" r="5" fill="#9bcb3c"/></svg>
    </div>
    <p class="service-text">Receive automatic notifications (upon request) whenever your favorite venue/activity is available.</p>
  </section>

  <section class="service s7">
    <div class="service-icon">
      <svg width="74" height="66" viewBox="0 0 74 66"><ellipse cx="37" cy="30" rx="34" ry="26" fill="#111"/><path d="M14 50l-4 14 16-9z" fill="#111"/><path d="M22 28h8v16h-8zM32 28l6-12c3 0 5 2 4 6l-1 5h10c3 0 4 3 3 5l-3 11c-1 2-2 3-4 3H32z" fill="#fff"/></svg>
    </div>
    <p class="service-text">Rate and post reviews about your experience</p>
  </section>

  <footer class="bottom-bar">
    <div class="contact">
      <svg width="24" height="28" viewBox="0 0 24 28"><path d="M6 2l5 6-3 3c1 4 4 8 8 10l3-3 5 5-4 4C10 26 1 14 2 6z" fill="#add136"/></svg>
      <span>+973-36550147</span>
    </div>
    <div class="contact">
      <svg width="30" height="22" viewBox="0 0 30 22"><rect x="2" y="2" width="26" height="18" fill="none" stroke="#add136" stroke-width="2.5"/><path d="M2 2l13 10L28 2" fill="none" stroke="#add136" stroke-width="2.5"/></svg>
      <span>support@goaldash.net</span>
    </div>
  </footer>
</main>
</body>
</html>
```